Lorna and Vikram Destination Wedding Invitation

THE DESIGN
- We need a unique, fun and colourful wedding invitation.
- We would like the designs to be printed using letterpress (not block) and or laser cut. Open to suggestions.
- We would like to include the attached wedding logo.
- We would like a design that is fun yet classy.
- 3D if possible.
- Main colour: deep purple; secondary colour: green.

Colour example:
http://www.bloomvowshop.com/Soft-Petal-Marigold-Sprays-Posyp/mkrtz412.htm
- we did think about using the following product to enclose the necessary cards. This is not mandatory. http://www.vowsandtiesstore.co.uk/product/willow-fold-invitation#colour=19

TO AVOID
- Paisleys
- Obvious flowers
- Block letterpress

FAVOURED DESIGNS
http://i0.wp.com/www.inkmorrow.com/images/blog-images/cedar-lantern1.jpg?resize=400%2C533
http://studioferlune.com/collection-corvane.html
http://studioferlune.com/collection-baldric.html
https://www.craftlymart.com/listing/847362915/fougere-wedding-invitation-laser-cut

THE COUPLE
- Bride: Lorna Maeve Castellanos
- Groom: Vikram Dalbeth
- Both from Sydney, Australia
- Both living in London, UK
- Website: lornaandvikram.com

THE WEDDING:
- We are getting married in Koh Samui, Thailand, early next year.
- We have 3 official events, the welcome drinks (March 25), the wedding (March 27) and beach bbq (March 28).

THE INVITE -1 CARD design
For everyone, a page/card that will include the following:
- Reception/ Main invite
- Location card (Direction/Map). Venue: Tharuvan Cove Spa Resort
- RSVP - via website
See wording attachment for details.

I need an insert (template) for the following: - 1 design only.
- Tide Lantern Night
- Tots Hollow (for people with children)
- Rehearsal

ADDITIONAL
- We would like the design to be adaptable for place cards and or wedding programs (normal printer).

Please let me know if you need more information.

Target Market(s)

Fun, casual, unique

Industry/Entity Type

Wedding

Colors
6b449b
876aae
b7a5cd

Requirements
Must have
• Wedding logo
Nice to have
• Please see project description
Should not have

```html
<!DOCTYPE html>
<html lang="en">
<head>
<meta charset="utf-8">
<title>Lorna &amp; Vikram – Wedding Invitation</title>
<link rel="stylesheet" href="https://fonts.googleapis.com/css2?family=Great+Vibes&family=Parisienne&family=Lato:ital,wght@0,400;1,400&display=swap">
<style>
  :root {
    --purple-deep: #4f2c7c;
    --purple-main: #6b449b;
    --purple-mid: #876aae;
    --purple-soft: #b7a5cd;
    --green-light: #7ddc63;
    --white: #ffffff;
    --ink-soft: #e9e1f3;
  }
  * { margin: 0; padding: 0; box-sizing: border-box; }
  html, body { width: 833px; height: 1200px; overflow: hidden; background: var(--purple-deep); }
  .invitation {
    position: relative;
    width: 833px;
    height: 1200px;
    overflow: hidden;
    color: var(--white);
    font-family: "Lato", sans-serif;
    background: radial-gradient(ellipse at 50% 45%, var(--purple-main) 0%, #5a3689 60%, var(--purple-deep) 100%);
  }
  .lace { position: absolute; left: 0; width: 833px; }
  .lace--top { top: 0; height: 190px; }
  .lace--bottom { bottom: 0; height: 170px; }

  .monogram {
    position: absolute;
    left: 354px; top: 175px;
    width: 125px; height: 125px;
    border-radius: 50%;
    background: var(--white);
    display: flex; align-items: center; justify-content: center;
    box-shadow: 0 0 0 4px rgba(255,255,255,0.25);
  }
  .monogram__name {
    font-family: "Great Vibes", cursive;
    font-size: 27px;
    line-height: 1.05;
    color: var(--purple-main);
    text-align: center;
  }

  .couple {
    position: absolute;
    top: 328px; left: 0; width: 833px; height: 160px;
  }
  .partner {
    position: absolute;
    top: 0;
    text-align: center;
    font-family: "Great Vibes", cursive;
    font-weight: 400;
    font-size: 44px;
    line-height: 56px;
    white-space: nowrap;
  }
  .partner--bride { left: 70px; width: 320px; }
  .partner--groom { left: 440px; width: 320px; }
  .ampersand {
    position: absolute; left: 386px; top: 0; width: 60px;
    text-align: center;
    font-family: "Great Vibes", cursive;
    font-size: 50px; line-height: 56px;
  }
  .parents {
    position: absolute; top: 128px;
    font-family: "Parisienne", cursive;
    font-size: 16px;
    line-height: 22px;
    color: var(--ink-soft);
    text-align: center;
  }
  .parents--bride { left: 70px; width: 320px; }
  .parents--groom { left: 440px; width: 320px; }

  .welcome {
    position: absolute; top: 512px; left: 0; width: 833px;
    text-align: center;
    font-family: "Parisienne", cursive;
    font-size: 24px; line-height: 32px;
  }
  .divider-dot {
    position: absolute; left: 411px;
    width: 11px; height: 11px; border-radius: 50%;
    background: var(--green-light);
  }

  .events { position: absolute; top: 640px; left: 150px; width: 560px; }
  .event {
    display: grid;
    grid-template-columns: 190px 1fr;
    align-items: center;
    height: 64px;
  }
  .event + .event { margin-top: 24px; }
  .event__date { font-family: "Great Vibes", cursive; line-height: 1; }
  .event__day { font-size: 26px; display: block; }
  .event__num { font-size: 46px; }
  .event__num sup { font-size: 22px; }
  .event__time { font-size: 28px; }
  .event__title { font-size: 15px; color: var(--white); }
  .event__venue { font-size: 12px; font-style: italic; color: var(--ink-soft); margin-top: 4px; }

  .closing {
    position: absolute; top: 912px; left: 0; width: 833px;
    text-align: center;
    font-family: "Parisienne", cursive;
    font-size: 24px; line-height: 34px;
  }
  .rsvp {
    position: absolute; top: 1040px; left: 0; width: 833px;
    text-align: center;
    font-family: "Parisienne", cursive;
    font-size: 21px;
  }
</style>
</head>
<body>
<main class="invitation">

  <svg class="lace lace--top" viewBox="0 0 833 190" role="img" aria-label="Green laser-cut lace ornament border along the top edge">
    <defs>
      <linearGradient id="laceTop" x1="0" y1="0" x2="0" y2="1">
        <stop offset="0" stop-color="#2f9a3b"/>
        <stop offset="1" stop-color="#6fd35a"/>
      </linearGradient>
    </defs>
    <path d="M0 0 H833 V120 C780 150 720 110 660 130 C600 150 560 105 500 120 C460 130 440 160 416 165 C392 160 372 130 333 120 C273 105 233 150 173 130 C113 110 53 150 0 120 Z" fill="url(#laceTop)"/>
  </svg>

  <div class="monogram">
    <span class="monogram__name">Lorna<br>&amp; Vikram</span>
  </div>

  <section class="couple">
    <h1 class="partner partner--bride">Lorna Maeve<br>Castellanos</h1>
    <span class="ampersand">&amp;</span>
    <h1 class="partner partner--groom">Vikram Arjun<br>Dalbeth</h1>
    <p class="parents parents--bride">Daughter of Marisol and Teodoro</p>
    <p class="parents parents--groom">Son of Anila and Devendra</p>
  </section>

  <p class="welcome">Please join us for a celebration of love,<br>friendship, laughter and family</p>
  <span class="divider-dot" style="top:600px"></span>

  <section class="events">
    <div class="event">
      <div class="event__date"><span class="event__day">march friday</span><span class="event__num">25<sup>th</sup></span> <span class="event__time">6:00pm</span></div>
      <div><p class="event__title">Welcome drinks and canapes</p><p class="event__venue">Tharuvan Cove Spa Resort, Maret, Koh Samui, Thailand</p></div>
    </div>
    <div class="event">
      <div class="event__date"><span class="event__day">march sunday</span><span class="event__num">27<sup>th</sup></span> <span class="event__time">4:00pm</span></div>
      <div><p class="event__title">Wedding ceremony</p><p class="event__venue">Tharuvan Cove Spa Resort, Maret, Koh Samui, Thailand</p></div>
    </div>
    <div class="event">
      <div class="event__date"><span class="event__day">march monday</span><span class="event__num">28<sup>th</sup></span> <span class="event__time">1:00pm</span></div>
      <div><p class="event__title">Beach BBQ Lunch</p><p class="event__venue">Tharuvan Cove Spa Resort, Maret, Koh Samui, Thailand</p></div>
    </div>
  </section>

  <span class="divider-dot" style="top:888px"></span>

  <p class="closing">Fabulous food, fun and festivities to follow<br>Dress code: colourful beach formal</p>

  <span class="divider-dot" style="top:1012px"></span>

  <p class="rsvp">Please RSVP by 1st November 2015 via website: lornaandvikram.com</p>

  <svg class="lace lace--bottom" viewBox="0 0 833 170" role="img" aria-label="Green laser-cut lace ornament border along the bottom edge">
    <defs>
      <linearGradient id="laceBottom" x1="0" y1="1" x2="0" y2="0">
        <stop offset="0" stop-color="#2f9a3b"/>
        <stop offset="1" stop-color="#6fd35a"/>
      </linearGradient>
    </defs>
    <path d="M0 170 H833 V40 C790 20 740 70 690 55 C640 40 600 90 540 80 C490 72 450 95 416 100 C382 95 343 72 293 80 C233 90 193 40 143 55 C93 70 43 20 0 40 Z" fill="url(#laceBottom)"/>
  </svg>

</main>
</body>
</html>
```